Webdesign für Immobilienmanagement
Zielgruppe
Immobilienmanagement Unternehmen / allg. Hausverwaltung , Hausmeisterservice, Grünanlagenpflege, Unterhaltsreinigung, Winterdienst
Zielgruppe: Mieter und Wohnungseigentümer
Aufgabenstellung
Farben: weiß/grün
keine Kopie der alten Seite
nutzerfreundliche Unternehmenswebseite
Logo vorhanden auf alter Webseite

```html
<!DOCTYPE html>
<html lang="de">
<head>
<meta charset="utf-8">
<title>Lindenhof Immobilien-Management</title>
<link href="https://fonts.googleapis.com/css2?family=Lato:wght@400;700;900&display=swap" rel="stylesheet">
<style>
:root{
  --dark:#1f3a14;
  --navbar:#172b0f;
  --lime:#a4ef74;
  --green:#4aa52e;
  --green-dark:#2e6b1c;
  --yellow:#f6c21c;
  --grey-band:#f1f1f1;
  --card:#f8f8f8;
  --line:#d8d8d8;
  --text:#333;
}
*{box-sizing:border-box;margin:0;padding:0}
html,body{width:714px;height:1200px;overflow:hidden;background:#fff}
body{position:relative;font-family:'Lato',sans-serif;color:var(--text)}
.abs{position:absolute}
.header{left:0;top:0;width:714px;height:54px;background:var(--dark)}
.brand{left:89px;top:15px;color:#fff;font-weight:900;font-size:20px;letter-spacing:.5px;display:flex;align-items:center;gap:6px}
.brand-square{width:14px;height:14px;background:var(--lime)}
.brand-sub{left:90px;top:39px;color:#fff;font-size:7px;font-weight:700}
.emergency{left:469px;top:13px;width:155px;height:31px;background:#f4f4f4;border-radius:3px}
.emergency-text{left:8px;top:5px;font-size:6px;line-height:8px;color:#333}
.emergency-text b{font-size:6.5px;color:#111}
.emergency-tag{left:104px;top:0;width:50px;height:38px;background:var(--yellow);clip-path:polygon(0 0,100% 0,100% 85%,50% 100%,0 85%);text-align:center;font-size:6.5px;font-weight:900;color:#222;padding-top:5px;line-height:8px}
.nav{left:0;top:54px;width:714px;height:30px;background:var(--navbar)}
.nav a{position:absolute;top:0;height:30px;line-height:30px;color:#fff;font-size:7px;font-weight:700;text-decoration:none}
.nav a.active{background:var(--lime);color:#1a2d10;text-align:center;width:50px;left:100px}
.hero{left:0;top:84px;width:714px;height:246px;background:linear-gradient(180deg,#eef2f0 0%,#e3e7d8 45%,#c8b85a 70%,#6f9a2c 85%,#7aa83a 100%)}
.hero h1{left:106px;top:70px;font-size:19.5px;line-height:23px;font-weight:700;color:#1c2c12}
.dots{left:337px;top:316px;display:flex;gap:5px}
.dots span{width:5px;height:5px;border-radius:50%;background:#fff}
.dots span:first-child{background:#222}
.services{left:0;top:330px;width:714px;height:74px;background:var(--grey-band)}
.svc{position:absolute;top:14px;text-align:center;font-size:7.2px;line-height:8.6px;color:#222}
.svc svg{display:block;margin:0 auto 6px;width:24px;height:24px}
.sep{position:absolute;top:14px;width:1px;height:50px;background:#ddd}
.about-img{left:118px;top:432px;width:176px;height:105px;background:linear-gradient(180deg,#b9cfd8 0%,#dfe6e6 35%,#6f8a55 60%,#3f6a2a 100%);clip-path:polygon(0 33%,50% 0,100% 33%,100% 100%,0 100%)}
h2.sec{font-size:11.5px;font-weight:700;color:var(--green)}
.about-text{left:327px;top:465px;width:265px;font-size:7.2px;line-height:10.7px}
.about-text p+p{margin-top:10.7px}
.card{position:absolute;top:609px;width:152px;height:191px;background:var(--card);border:1px solid var(--line)}
.card-img{height:105px}
.card h3{margin:8px 0 0 12px;font-size:9.2px;font-weight:700;color:var(--green)}
.card ul{list-style:none;margin:5px 0 0 12px;font-size:7.2px;line-height:10.7px}
.card li::before{content:"»";margin-right:5px;font-size:6px}
.more{position:absolute;left:14px;bottom:-7px;width:44px;height:14px;background:var(--green);color:#fff;font-size:7px;font-weight:700;line-height:14px;text-align:center;border-radius:2px}
.callback{left:109px;top:825px;width:496px;height:109px;border-radius:3px;background:linear-gradient(90deg,#4c9a34 0%,#3f8a2a 45%,#1c3a12 100%);overflow:hidden}
.callback h2{left:16px;top:28px;font-size:13.5px;color:#fff;font-weight:700}
.callback p{left:16px;top:45px;font-size:6.8px;color:#fff}
.field{position:absolute;top:61px;width:111px;height:17px;border-radius:9px;background:#fff;font-size:7px;line-height:17px;padding-left:11px;color:#333}
.send{position:absolute;top:61px;left:364px;width:75px;height:17px;border-radius:9px;background:var(--yellow);font-size:7.5px;line-height:17px;text-align:center;color:#333;font-weight:700}
.reviews-title{left:0;top:955px;width:714px;text-align:center;font-size:16px;font-weight:700;color:#1c2c12}
.quote{position:absolute;top:993px;width:217px;height:70px;background:#f8f8f8;border:1px solid var(--line);padding:12px 12px;font-size:7.2px;line-height:10.7px}
.tail{position:absolute;top:1062px}
.author{position:absolute;top:1079px;font-size:7.5px;font-weight:700;color:#111}
.arrow{position:absolute;top:1016px;width:20px;height:20px;border:1px solid #555;border-radius:50%}
.arrow svg{position:absolute;left:5px;top:5px}
.footer{left:0;top:1123px;width:714px;height:77px;background:var(--dark);text-align:center;font-size:6.8px}
.footer .a{position:absolute;top:16px;width:100%;color:var(--green)}
.footer .b{position:absolute;top:27px;width:100%;color:#fff}
.footer .c{position:absolute;top:43px;width:100%;color:var(--green)}
</style>
</head>
<body>

<header class="abs header">
  <div class="abs brand">LINDENHOF <span class="brand-square"></span></div>
  <div class="abs brand-sub">IMMOBILIEN - MANAGEMENT GMBH</div>
  <div class="abs emergency">
    <div class="abs emergency-text"><b>NOTDIENST</b><br>24 Std. am Tag und auch an<br>den Wochenenden!</div>
    <div class="abs emergency-tag">
      <svg width="10" height="8" viewBox="0 0 10 8"><circle cx="6" cy="4" r="3.2" fill="none" stroke="#222" stroke-width=".8"/><path d="M6 2.3V4l1 .8M0 2h2M0 4h2M0 6h2" stroke="#222" stroke-width=".8" fill="none"/></svg><br>24 STD<br>NOTDIENST
    </div>
  </div>
</header>

<nav class="abs nav">
  <a class="active" href="#">HOME</a>
  <a href="#" style="left:169px">UBER UNS</a>
  <a href="#" style="left:233px">HAUSVERWALTUNG</a>
  <a href="#" style="left:330px">HAUSMEISTER</a>
  <a href="#" style="left:408px">DOWNLOADS</a>
  <a href="#" style="left:485px">PARTNERLINKS</a>
  <a href="#" style="left:566px">KONTAKT</a>
</nav>

<section class="abs hero" role="img" aria-label="Park mit Bäumen und Rasen im Sonnenlicht, dahinter eine Hochhaus-Skyline">
  <h1 class="abs">Ihr zuverlässiger Dienstleister<br>rund um die Immobilie</h1>
</section>
<div class="abs dots"><span></span><span></span><span></span><span></span><span></span></div>

<section class="abs services">
  <div class="svc" style="left:105px;width:62px"><svg viewBox="0 0 24 24" fill="none" stroke="#222" stroke-width="1"><path d="M2 16h5l5 2 8-4-2-2-6 2M2 22h6l10-3"/><rect x="8" y="5" width="9" height="7"/><path d="M7 6l5-4 6 4"/></svg>Allgemeine<br>Hausverwaltung</div>
  <div class="sep" style="left:172px"></div>
  <div class="svc" style="left:178px;width:58px"><svg viewBox="0 0 24 24" fill="none" stroke="#222" stroke-width="1"><circle cx="12" cy="8" r="5"/><path d="M4 23c0-6 4-9 8-9s8 3 8 9z"/></svg>Kaufmännische<br>Betreuung</div>
  <div class="sep" style="left:240px"></div>
  <div class="svc" style="left:245px;width:48px"><svg viewBox="0 0 24 24" fill="none" stroke="#222" stroke-width="1"><circle cx="11" cy="11" r="7"/><circle cx="11" cy="11" r="3"/><path d="M11 2v3M11 17v3M2 11h3M17 11h3"/></svg>Technische<br>Betreuung</div>
  <div class="sep" style="left:296px"></div>
  <div class="svc" style="left:302px;width:72px"><svg viewBox="0 0 24 24" fill="none" stroke="#222" stroke-width="1"><path d="M3 4l10 10M6 21l8-8 4 4-8 8zM16 4l4 4"/></svg>Hausmeisterservice</div>
  <div class="sep" style="left:380px"></div>
  <div class="svc" style="left:386px;width:68px"><svg viewBox="0 0 24 24" fill="none" stroke="#222" stroke-width="1"><path d="M2 21h20M6 21v-4M10 21v-6M14 21l4-14M18 7l3-3"/></svg>Grünanlagenpflege</div>
  <div class="sep" style="left:460px"></div>
  <div class="svc" style="left:466px;width:74px"><svg viewBox="0 0 24 24" fill="none" stroke="#222" stroke-width="1"><path d="M3 12l8-7 8 7v10H3z"/><rect x="6" y="14" width="4" height="4"/><path d="M14 22v-6h3v6M16 8l6-6"/></svg>Unterhaltsreinigung</div>
  <div class="sep" style="left:545px"></div>
  <div class="svc" style="left:551px;width:52px"><svg viewBox="0 0 24 24" fill="none" stroke="#222" stroke-width="1"><path d="M12 1v22M2.5 6.5l19 11M2.5 17.5l19-11M9 2l3 3 3-3M9 22l3-3 3 3"/></svg>Winterdienst</div>
</section>

<div class="abs about-img" role="img" aria-label="Modernes weißes Einfamilienhaus mit Garten unter einem Dachgiebel"></div>
<h2 class="abs sec" style="left:327px;top:437px">WER WIR SIND</h2>
<div class="abs about-text">
  <p>Wir sind ein junges, freundliches, gut ausgebildetes Team, das sich mit all seiner Aufmerksamkeit und Kompetenz um Ihre Wünsche in Sachen Immobilien kümmert. Möchten Sie eine Wohnung mieten, suchen Sie einen Hausmeister ... oder einen Verwalter für Ihre Immobilie?</p>
  <p>Schauen Sie sich unser Leistungsangebot an und überzeugen Sie sich selbst von den Vorteilen, die wir Ihnen bieten können.</p>
</div>

<h2 class="abs sec" style="left:0;top:579px;width:714px;text-align:center">WAS WIR TUN</h2>

<div class="card" style="left:109px">
  <div class="card-img" role="img" aria-label="Gelbes Holzhaus mit Baum im Vorgarten" style="background:linear-gradient(180deg,#d9dcd5,#d7b574 50%,#4f7a32)"></div>
  <h3>Hausverwaltung</h3>
  <ul><li>Allgemeine Verwaltung</li><li>Kaufmännische Betreuung</li><li>Technische Betreuung</li></ul>
  <div class="more">Mehr ...</div>
</div>
<div class="card" style="left:281px">
  <div class="card-img" role="img" aria-label="Zwei Handwerker mit Helm und Warnweste prüfen einen Bauplan" style="background:linear-gradient(180deg,#e4e6e8,#e0894a 50%,#3a5e8a)"></div>
  <h3>Hausmeister</h3>
  <ul><li>Hausmeisterservice</li><li>Grünanlagenpflege</li><li>Winterdienst</li><li>Unterhaltsreinigung</li></ul>
  <div class="more">Mehr ...</div>
</div>
<div class="card" style="left:453px">
  <div class="card-img" role="img" aria-label="Installateur repariert Rohre unter einer Spüle" style="background:linear-gradient(180deg,#e8e6e2,#8a8177 45%,#2f52a8)"></div>
  <h3>Notdienst</h3>
  <ul><li>Schnell &amp; kompetent</li><li>24 Stunden am Tag, 7 Tage die Woche</li></ul>
  <div class="more">Mehr ...</div>
</div>

<section class="abs callback">
  <svg class="abs" style="left:160px;top:5px" width="120" height="100" viewBox="0 0 120 100" fill="none" stroke="rgba(0,0,0,.12)" stroke-width="10"><path d="M20 10c-10 10 0 45 30 70s55 25 60 15l-20-20-15 8c-12-6-22-18-28-30l8-15z"/><path d="M60 12a40 40 0 0 1 40 40M60 30a22 22 0 0 1 22 22"/></svg>
  <h2 class="abs">Fordern Sie einen Rückruf an</h2>
  <p class="abs">Sie haben eine Frage zu unserem Serviceangebot? Dann füllen Sie einfach folgendes Formular aus und wir melden uns schnellst-möglich bei Ihnen.</p>
  <div class="field" style="left:16px">Name:</div>
  <div class="field" style="left:132px">E-Mail:</div>
  <div class="field" style="left:248px">Telefon:</div>
  <div class="send">SENDEN</div>
</section>

<h2 class="abs reviews-title">Was unser Kunde sagt</h2>
<div class="arrow" style="left:99px"><svg width="9" height="9" viewBox="0 0 9 9"><path d="M6 1L2.5 4.5 6 8" stroke="#333" fill="none"/></svg></div>
<div class="quote" style="left:126px">Lorem ipsum dolor sit amet, consectetur adipiscing elit, sed do eiusmod tempor incididunt ut labore et dolore magna aliqua. Quis ipsum suspendisse ultrices gravida. Risus commodo viverra maecenas accumsan lacus vel facilisis.</div>
<svg class="tail" style="left:174px" width="28" height="11" viewBox="0 0 28 11"><path d="M0 0L2 10 24 0" fill="#f8f8f8" stroke="#d8d8d8"/><path d="M1 0h23" stroke="#f8f8f8" stroke-width="2"/></svg>
<div class="author" style="left:141px">- Maren Kolb</div>
<div class="quote" style="left:367px">Lorem ipsum dolor sit amet, consectetur adipiscing elit, sed do eiusmod tempor incididunt ut labore et dolore magna aliqua. Quis ipsum suspendisse ultrices gravida. Risus commodo viverra maecenas accumsan lacus vel facilisis.</div>
<svg class="tail" style="left:415px" width="28" height="11" viewBox="0 0 28 11"><path d="M0 0L2 10 24 0" fill="#f8f8f8" stroke="#d8d8d8"/><path d="M1 0h23" stroke="#f8f8f8" stroke-width="2"/></svg>
<div class="author" style="left:382px">- Maren Kolb</div>
<div class="arrow" style="left:592px"><svg width="9" height="9" viewBox="0 0 9 9"><path d="M3 1l3.5 3.5L3 8" stroke="#333" fill="none"/></svg></div>

<footer class="abs footer">
  <div class="a">Lindenhof Immobilien-Management GmbH • Birkenweg 7 • 04100 Musterstadt</div>
  <div class="b">Telephone: 03412/555-0 • Fax: 03412/555-45 • Email: info@lindenhof-immo.example</div>
  <div class="c">Impressum &nbsp;|&nbsp; Datenschutz</div>
</footer>

</body>
</html>
```